Velmora business card design

Design a business card for a cryptocurrency company that uses the attached logo. Some example business cards to give you guys a flavor of what we're looking for is given below (of course feel free to be creative):
https://www.plimtorque.com/studio.aspx?template=5813490_KT4&ag=True&xnav=HSG_Design_Image&rd=1
https://www.plimtorque.com/studio.aspx?template=7240615_KT4&ag=True&xnav=HSG_Design_Image&rd=1
The business card should be clean/simple and convey the company name, what we're about and the specific persons contact info. In terms of what we're about, we can have our name Velmora, with a line under it that says "Cryptocurrency visualization, analytics, and trading"
We want something futuristic looking but simple / clean.
The color scheme for the logo should be used.
The name of the person and their title should be editable, so we can use the business card design for multiple people.
(Please use the zip file to get the vector graphics and different image formats)

```html
<!DOCTYPE html>
<html lang="en">
<head>
<meta charset="utf-8">
<title>Velmora business card</title>
<link rel="stylesheet" href="https://fonts.googleapis.com/css2?family=Exo+2:wght@700;800&family=Roboto:wght@400;500&display=swap">
<style>
  :root {
    --backdrop: #3b3c3e;
    --navy: #10213d;
    --navy-soft: #16304f;
    --white: #fbfcfd;
    --blue: #1a7be6;
    --teal: #17b6c9;
    --green: #27e08a;
    --ink: #132441;
  }
  * { margin: 0; padding: 0; box-sizing: border-box; }
  html, body { width: 799px; height: 1200px; overflow: hidden; }
  body {
    background: var(--backdrop);
    position: relative;
    font-family: "Roboto", sans-serif;
  }
  .card {
    position: absolute;
    left: 80px;
    width: 640px;
    height: 366px;
    border-radius: 26px;
    overflow: hidden;
    box-shadow: 0 14px 30px rgba(0,0,0,.45);
  }
  .card-front {
    top: 140px;
    background: linear-gradient(135deg, var(--navy-soft), var(--navy) 60%);
    display: flex;
    align-items: center;
    justify-content: center;
  }
  .front-wordmark {
    font-family: "Exo 2", sans-serif;
    font-weight: 800;
    font-size: 78px;
    letter-spacing: 6px;
    color: #ffffff;
  }
  .card-back {
    top: 700px;
    background: var(--white);
  }
  .back-waves {
    position: absolute;
    inset: 0;
    width: 100%;
    height: 100%;
  }
  .brand {
    position: absolute;
    left: 42px;
    top: 30px;
    display: flex;
    align-items: center;
    gap: 16px;
  }
  .brand-mark {
    width: 46px;
    height: 46px;
    border-radius: 50%;
    background: var(--teal);
  }
  .brand-name {
    font-family: "Exo 2", sans-serif;
    font-weight: 800;
    font-size: 54px;
    letter-spacing: 5px;
    color: var(--ink);
  }
  .person {
    position: absolute;
    left: 50px;
    top: 112px;
  }
  .person-name {
    font-family: "Exo 2", sans-serif;
    font-weight: 700;
    font-size: 23px;
    color: var(--ink);
  }
  .person-title {
    font-size: 14px;
    color: var(--ink);
    margin-top: 2px;
  }
  .contacts {
    position: absolute;
    right: 34px;
    top: 240px;
    list-style: none;
    text-align: right;
    color: #ffffff;
    font-size: 15px;
  }
  .contacts li {
    display: flex;
    justify-content: flex-end;
    align-items: center;
    gap: 10px;
    line-height: 24px;
  }
  .contact-icon {
    width: 14px;
    height: 14px;
    border-radius: 50%;
    background: linear-gradient(135deg, var(--blue), var(--green));
  }
  .address {
    position: absolute;
    right: 34px;
    bottom: 16px;
    color: #ffffff;
    font-size: 14px;
  }
</style>
</head>
<body>
  <section class="card card-front">
    <span class="front-wordmark">VELMORA</span>
  </section>

  <section class="card card-back">
    <svg class="back-waves" viewBox="0 0 640 366" preserveAspectRatio="none" aria-hidden="true">
      <defs>
        <linearGradient id="wave-stroke" x1="0" x2="1" y1="0" y2="0">
          <stop offset="0" stop-color="#1a7be6"/>
          <stop offset="0.5" stop-color="#17b6c9"/>
          <stop offset="1" stop-color="#27e08a"/>
        </linearGradient>
      </defs>
      <path d="M0 188 C120 250 240 252 380 225 C480 208 570 195 640 215 L640 366 L0 366 Z" fill="#10213d"/>
      <path d="M0 168 C110 232 230 234 380 205 C480 188 570 178 640 200 L640 215 C570 195 480 208 380 225 C240 252 120 250 0 188 Z" fill="url(#wave-stroke)"/>
      <path d="M30 212 C140 250 240 254 350 240" fill="none" stroke="#ffffff" stroke-width="2.5"/>
    </svg>

    <div class="brand">
      <span class="brand-mark"></span>
      <span class="brand-name">VELMORA</span>
    </div>

    <div class="person">
      <p class="person-name">Jane Mira Holt</p>
      <p class="person-title">Managing Director</p>
    </div>

    <ul class="contacts">
      <li>555.014.2387 <span class="contact-icon"></span></li>
      <li>www.velmora-crypto.com <span class="contact-icon"></span></li>
      <li>janeholt@velmora-crypto.com <span class="contact-icon"></span></li>
    </ul>

    <p class="address">71 Larkfield Rd., Brookvale, Elm County, US 482019</p>
  </section>
</body>
</html>
```